Business Card for Bright Lantern

Please design a Modern Business card for a Online Marketing Company

Website: http://www.brightlantern-example.com.au

Please do NOT include physical address in design.

Industry/Entity Type

Business

```html
<!DOCTYPE html>
<html lang="en">
<head>
<meta charset="utf-8">
<title>Bright Lantern – Business Card</title>
<link href="https://fonts.googleapis.com/css2?family=Open+Sans:ital,wght@0,400;0,600;1,400&family=Roboto:wght@400;700&display=swap" rel="stylesheet">
<style>
  :root {
    --brand-red: #d01f36;
    --brand-red-dark: #b3182d;
    --paper: #f6f6f6;
    --ink: #1e1e1e;
    --ink-soft: #3a3a3a;
    --white: #ffffff;
    --backdrop: #e4e1dc;
  }
  * { box-sizing: border-box; margin: 0; padding: 0; }
  html, body {
    width: 1200px;
    height: 1000px;
    overflow: hidden;
    background: var(--backdrop);
  }
  .sheet {
    width: 1200px;
    height: 1000px;
    display: flex;
    flex-direction: column;
    align-items: center;
    justify-content: center;
    gap: 60px;
  }
  .card {
    position: relative;
    width: 600px;
    height: 343px;
    overflow: hidden;
    box-shadow: 0 10px 30px rgba(0,0,0,0.18);
  }

  /* Front side */
  .card-front { background: var(--paper); }
  .card-front .wave {
    position: absolute;
    inset: 0;
    width: 100%;
    height: 100%;
  }
  .front-brand {
    position: absolute;
    left: 26px;
    top: 112px;
    display: flex;
    align-items: center;
    gap: 7px;
    font-family: "Roboto", sans-serif;
    font-weight: 700;
    font-size: 12px;
    color: var(--white);
    text-transform: uppercase;
    letter-spacing: 0.5px;
  }
  .brand-square {
    width: 12px;
    height: 12px;
    background: var(--white);
  }
  .person {
    position: absolute;
    left: 300px;
    top: 52px;
    font-family: "Open Sans", sans-serif;
  }
  .person-name {
    font-size: 34px;
    font-weight: 400;
    color: var(--ink);
    letter-spacing: 0.5px;
  }
  .person-role {
    font-size: 12px;
    font-style: italic;
    color: var(--ink-soft);
    margin-top: 2px;
    margin-left: 4px;
  }
  .contacts {
    position: absolute;
    left: 318px;
    top: 226px;
    list-style: none;
    font-family: "Open Sans", sans-serif;
    font-size: 12.5px;
    color: var(--white);
  }
  .contacts li {
    display: flex;
    align-items: center;
    gap: 8px;
    height: 26px;
  }
  .contacts .icon { width: 16px; height: 16px; flex: none; }

  /* Back side */
  .card-back { background: var(--brand-red); }
  .back-brand {
    position: absolute;
    left: 0;
    right: 0;
    top: 128px;
    display: flex;
    flex-direction: column;
    align-items: center;
    font-family: "Roboto", sans-serif;
  }
  .back-brand-row {
    display: flex;
    align-items: center;
    gap: 14px;
  }
  .back-brand .brand-square {
    width: 30px;
    height: 30px;
  }
  .company-name {
    font-size: 32px;
    font-weight: 700;
    color: var(--white);
    text-transform: uppercase;
    letter-spacing: 0.5px;
  }
  .tagline {
    margin-top: 6px;
    margin-left: 44px;
    font-size: 15px;
    font-weight: 400;
    color: var(--ink);
  }
</style>
</head>
<body>
<main class="sheet">

  <section class="card card-front" aria-label="Business card front">
    <svg class="wave" viewBox="0 0 600 343" preserveAspectRatio="none" aria-hidden="true">
      <path d="M0,96 C140,58 290,110 410,168 C490,206 550,204 600,196 L600,343 L0,343 Z" fill="var(--brand-red)"/>
    </svg>

    <div class="front-brand"><span class="brand-square"></span>Bright Lantern</div>

    <div class="person">
      <h1 class="person-name">Daniel Reyes</h1>
      <p class="person-role">Marketing Manager</p>
    </div>

    <ul class="contacts">
      <li>
        <svg class="icon" viewBox="0 0 16 16" aria-hidden="true">
          <circle cx="8" cy="8" r="8" fill="var(--white)"/>
          <path d="M5.2,4 L6.8,4 L7.3,6 L6.3,6.8 C6.8,8 7.8,9 9,9.6 L9.8,8.6 L11.8,9.1 L11.8,10.7 C8,11 4.8,7.8 5.2,4 Z" fill="var(--brand-red)"/>
        </svg>
        <span>0400 612 947</span>
      </li>
      <li>
        <svg class="icon" viewBox="0 0 16 16" aria-hidden="true">
          <circle cx="8" cy="8" r="8" fill="var(--white)"/>
          <rect x="4" y="5" width="8" height="6" fill="none" stroke="var(--brand-red)" stroke-width="1.2"/>
          <path d="M4,5 L8,8.5 L12,5" fill="none" stroke="var(--brand-red)" stroke-width="1.2"/>
        </svg>
        <span>hello@brightlantern-example.com.au</span>
      </li>
      <li>
        <svg class="icon" viewBox="0 0 16 16" aria-hidden="true">
          <circle cx="8" cy="8" r="8" fill="var(--white)"/>
          <circle cx="8" cy="8" r="4" fill="none" stroke="var(--brand-red)" stroke-width="1.1"/>
          <ellipse cx="8" cy="8" rx="1.8" ry="4" fill="none" stroke="var(--brand-red)" stroke-width="1"/>
          <line x1="4" y1="8" x2="12" y2="8" stroke="var(--brand-red)" stroke-width="1"/>
        </svg>
        <span>www.brightlantern-example.com.au</span>
      </li>
    </ul>
  </section>

  <section class="card card-back" aria-label="Business card back">
    <div class="back-brand">
      <div class="back-brand-row">
        <span class="brand-square"></span>
        <h2 class="company-name">Bright Lantern</h2>
      </div>
      <p class="tagline">Shine online - Grow online</p>
    </div>
  </section>

</main>
</body>
</html>
```